Corporate Design für Bauingenieur
Zielgruppe
Es geht hier um einen Bauingenieur mit den Schwerpunkten Energieberatung, Schallschutz, Wärmeschutz und BTH-Fördermittel-Beratung. Die Zielgruppe sind überwiegend Generalbauunternehmen, Architekten aber auch Firmen wie Norvita u. Lumo für die bereits gearbeitet wurde.
Aufgabenstellung
Konkrete Vorstellungen haben wir nicht, daher bewegen wir uns auch auf diesem Portal - wohl aber können wir sagen, dass das Logo schon hochwertige sein soll. Im Sinne von Vertrauen u. vertrauensvolle Arbeit, sowie Zuverlässigkeit usw. Also nicht exklusiv im Sinne eines kreativen Architekten sondern ehr kompetent.

```html
<!DOCTYPE html>
<html lang="de">
<head>
<meta charset="utf-8">
<title>Brenning Bauingenieur – Geschäftsausstattung</title>
<link href="https://fonts.googleapis.com/css2?family=Montserrat:wght@500;600&family=Source+Sans+3:wght@400;600&display=swap" rel="stylesheet">
<style>
  :root {
    --bg: #e6e7e9;
    --paper: #f4f4f5;
    --teal: #1a8fa8;
    --navy: #1e2433;
    --ink: #2a2a2a;
    --muted: #555a60;
    --window: #e9eaeb;
  }
  * { box-sizing: border-box; margin: 0; padding: 0; }
  html, body { width: 1200px; height: 1200px; overflow: hidden; background: var(--bg); }
  body { position: relative; font-family: "Source Sans 3", Arial, sans-serif; color: var(--ink); }

  .sheet { position: absolute; background: var(--paper); }

  .brand { position: absolute; display: flex; align-items: center; gap: 8px; }
  .brand-square { background: var(--teal); flex: none; }
  .brand-name {
    font-family: "Montserrat", Arial, sans-serif; font-weight: 600;
    color: var(--teal); text-transform: uppercase; line-height: 1.1; letter-spacing: .02em;
  }
  .brand-lg .brand-square { width: 30px; height: 30px; }
  .brand-lg .brand-name { font-size: 13.5px; }
  .brand-sm .brand-square { width: 14px; height: 14px; }
  .brand-sm .brand-name { font-size: 6.5px; }
  .brand-xs .brand-square { width: 10px; height: 10px; }
  .brand-xs .brand-name { font-size: 5px; }
  .on-dark .brand-name, .on-teal .brand-name { color: #fff; }
  .on-dark .brand-square, .on-teal .brand-square { background: #fff; }

  .contact-tab {
    position: absolute; background: var(--teal); color: #fff;
    display: flex; align-items: center; justify-content: space-around;
    font-size: 5.5px; border-radius: 2px 2px 0 0; padding: 0 6px;
  }
  .contact-tab span { display: flex; align-items: center; gap: 3px; }
  .contact-tab svg { width: 6px; height: 6px; fill: #fff; }

  /* Visitenkarten */
  .card-front { left: 80px; top: 258px; width: 213px; height: 121px; overflow: hidden; }
  .card-photo { position: absolute; inset: 0; background: linear-gradient(135deg, #2b3550 0%, #1a2236 55%, #141a2a 100%); }
  .card-front .brand { left: 58px; top: 52px; }
  .card-back { left: 326px; top: 258px; width: 212px; height: 121px; }
  .card-back .brand { left: 20px; top: 54px; }
  .card-divider { position: absolute; left: 106px; top: 30px; width: 1px; height: 61px; background: var(--teal); }
  .card-details { position: absolute; left: 112px; top: 30px; font-size: 4.8px; line-height: 1.3; color: var(--muted); }
  .card-details .card-title { color: var(--teal); font-weight: 600; margin-bottom: 5px; }
  .card-details li { list-style: none; display: flex; gap: 4px; margin-bottom: 4px; }
  .card-details svg { width: 5px; height: 5px; fill: var(--teal); flex: none; margin-top: 1px; }

  /* Umschläge */
  .envelope-front { left: 80px; top: 414px; width: 461px; height: 228px; }
  .envelope-front .brand { left: 46px; top: 40px; }
  .address-window { position: absolute; left: 46px; top: 122px; width: 201px; height: 76px; border-radius: 8px; background: var(--window); }
  .sender { position: absolute; left: 339px; top: 167px; font-size: 4.8px; line-height: 1.35; color: var(--muted); }
  .sender strong { display: block; color: var(--teal); font-weight: 600; margin-bottom: 6px; }

  .envelope-back { left: 80px; top: 682px; width: 461px; height: 230px; }
  .envelope-flap { position: absolute; left: 0; top: 0; width: 461px; height: 58px; background: var(--teal); border-radius: 0 0 12px 12px; }
  .envelope-flap .brand { left: 188px; top: 22px; }
  .envelope-back .contact-tab { left: 148px; top: 216px; width: 166px; height: 14px; }

  /* Briefbogen */
  .letterhead { left: 597px; top: 256px; width: 463px; height: 656px; }
  .letterhead .contact-tab { left: 265px; top: 0; width: 176px; height: 14px; border-radius: 0 0 2px 2px; }
  .letterhead .brand { left: 45px; top: 50px; }
  .letter-body { position: absolute; left: 43px; top: 164px; width: 370px; font-size: 9.2px; line-height: 15.6px; color: var(--ink); }
  .letter-body p { text-align: justify; margin-bottom: 15.6px; }
  .signature-area { position: absolute; left: 45px; top: 436px; width: 110px; height: 40px; background: #f0e4e4; border-radius: 4px; }
  .letter-footer { position: absolute; left: 45px; top: 578px; width: 390px; height: 34px; font-size: 5px; line-height: 1.45; color: var(--muted); }
  .footer-col { position: absolute; top: 0; }
  .footer-col h4 { color: var(--teal); font-weight: 600; font-size: 5px; margin-bottom: 9px; }
  .footer-col.ruled { border-left: 1px solid var(--muted); padding-left: 5px; height: 34px; }
</style>
</head>
<body>

<svg width="0" height="0" style="position:absolute">
  <defs>
    <symbol id="icon-phone" viewBox="0 0 24 24"><path d="M6.6 10.8a15 15 0 0 0 6.6 6.6l2.2-2.2a1 1 0 0 1 1-.25 11.4 11.4 0 0 0 3.6.57 1 1 0 0 1 1 1V20a1 1 0 0 1-1 1A17 17 0 0 1 3 4a1 1 0 0 1 1-1h3.5a1 1 0 0 1 1 1c0 1.25.2 2.45.57 3.57a1 1 0 0 1-.25 1z"/></symbol>
    <symbol id="icon-send" viewBox="0 0 24 24"><path d="M22 2 2 10l7 3 3 7z"/></symbol>
    <symbol id="icon-home" viewBox="0 0 24 24"><path d="M12 3 2 12h3v8h5v-5h4v5h5v-8h3z"/></symbol>
    <symbol id="icon-mail" viewBox="0 0 24 24"><path d="M2 5h20v14H2zm2 2v.5l8 5 8-5V7z"/></symbol>
    <symbol id="icon-globe" viewBox="0 0 24 24"><circle cx="12" cy="12" r="10"/></symbol>
  </defs>
</svg>

<!-- Visitenkarte Vorderseite -->
<section class="sheet card-front">
  <div class="card-photo" role="img" aria-label="Dunkel getöntes Architekturfoto eines Bürogebäudes"></div>
  <div class="brand brand-sm on-dark">
    <span class="brand-square"></span>
    <span class="brand-name">Lars Brenning<br>Bauingenieur</span>
  </div>
</section>

<!-- Visitenkarte Rückseite -->
<section class="sheet card-back">
  <div class="brand brand-xs">
    <span class="brand-square"></span>
    <span class="brand-name">Lars Brenning<br>Bauingenieur</span>
  </div>
  <div class="card-divider"></div>
  <ul class="card-details">
    <li class="card-title">Dipl.-Ing. (FH) Lars Brenning</li>
    <li><svg><use href="#icon-home"/></svg><span>Lindenweg 14<br>D-48000 Feldstadt</span></li>
    <li><svg><use href="#icon-phone"/></svg><span>+49 (0) 170. 000 412 7</span></li>
    <li><svg><use href="#icon-mail"/></svg><span>info@brenning-ingenieur.de</span></li>
    <li><svg><use href="#icon-globe"/></svg><span>www.brenning-ingenieur.de</span></li>
  </ul>
</section>

<!-- Briefumschlag Vorderseite -->
<section class="sheet envelope-front">
  <div class="brand brand-lg">
    <span class="brand-square"></span>
    <span class="brand-name">Lars Brenning<br>Bauingenieur</span>
  </div>
  <div class="address-window"></div>
  <div class="sender">
    <strong>Brenning Bauingenieur</strong>
    Dipl.-Ing. (FH) Lars Brenning<br>Lindenweg 14<br>D-48000 Feldstadt
  </div>
</section>

<!-- Briefumschlag Rückseite -->
<section class="sheet envelope-back">
  <div class="envelope-flap">
    <div class="brand brand-sm on-teal">
      <span class="brand-square"></span>
      <span class="brand-name">Lars Brenning<br>Bauingenieur</span>
    </div>
  </div>
  <div class="contact-tab">
    <span><svg><use href="#icon-phone"/></svg>+49 (0) 170. 000 412 7</span>
    <span><svg><use href="#icon-send"/></svg>info@brenning-ingenieur.de</span>
  </div>
</section>

<!-- Briefbogen -->
<section class="sheet letterhead">
  <div class="contact-tab">
    <span><svg><use href="#icon-phone"/></svg>+49 (0) 170. 000 412 7</span>
    <span><svg><use href="#icon-send"/></svg>info@brenning-ingenieur.de</span>
  </div>
  <div class="brand brand-lg">
    <span class="brand-square"></span>
    <span class="brand-name">Lars Brenning<br>Bauingenieur</span>
  </div>
  <div class="letter-body">
    <p>Dear Customers,</p>
    <p>Lorem ipsum dolor sit amet, consectetur adipiscing elit. Nunc varius, lectus vel eleifend vulputate, tortor diam sollicitudin mauris, vitae finibus diam est at sem. Aliquam mattis in mauris vel porta. Praesent volutpat lacus non massa sagittis, id eleifend sapien vestibulum. Etiam pretium odio rutrum semper scelerisque. Vestibulum tortor ligula, bibendum non dictum vitae, luctus eget massa.</p>
    <p>Lorem ipsum dolor sit amet, consectetur adipiscing elit. Suspendisse dapibus nunc eu molestie condimentum. Sed quis dolor non lorem lobortis convallis. Sed pretium erat ac tellus dapibus tempus. Maecenas semper erat id dictum tempor. Sed quis urna a orci luctus porta. Nam tempus libero mollis erat gravida, eget ullamcorper tortor commodo.</p>
    <p>Sincerely yours,</p>
  </div>
  <div class="signature-area" role="img" aria-label="Platz für die handschriftliche Unterschrift"></div>
  <footer class="letter-footer">
    <div class="footer-col" style="left:0">
      <h4>Brenning Bauingenieur</h4>
      Dipl.-Ing. (FH) Lars Brenning<br>Lindenweg 14<br>D-48000 Feldstadt
    </div>
    <div class="footer-col ruled" style="left:95px">
      <h4>Kontaktdaten</h4>
      Telefon: +49 (0) 170. 000 412 7<br>Email: info@brenning-ingenieur.de<br>Online: www.brenning-ingenieur.de
    </div>
    <div class="footer-col ruled" style="left:226px">
      <h4>Bürozeiten</h4>
      montag bis Freitag von<br>8.00 bis 18.00 Uhr<br>samstags geschlossen
    </div>
    <div class="footer-col" style="left:316px">
      <h4>Service Menü</h4>
      Datenschutzerklärung<br>Impressum<br>Haftungsbeschränkung
    </div>
  </footer>
</section>

</body>
</html>
```